Need modern simple design for magazine ad, apartment and condo roofer.

I need a half page magazine ad for a local roofer to publish in an industry magazine. Apartment associations industry. All types of roofs. Shingle and Flat
Need the design to be creative and modern, clean and simple. I do not want a busy design. One that stands out and makes a point quickly.
Logo must be prominent.
DO NOT USE PHOTOS FROM MY WEBSITE PLEASE. Looking for something new.
I work on entire complexes not houses.

Need to make sure our phone number and email address are listed at the bottom. Here is my website www.vorbelan.com
Want to stay away from standard clip arts of tools, homes, apartment buildings.
Half Horizontal 7.25 x 4.75
Ads should be in PDF and JPG format.

Target Market(s)

Apartment or Condo owners looking for large scale roofing projects

Industry/Entity Type

Roofing

Requirements
Must have
• Prominent Logo
Simple Clean Design
Create graphics
Not Busy
Should not have
• Clip Art
No Photos from my website

```html
<!DOCTYPE html>
<html lang="en">
<head>
<meta charset="utf-8">
<title>Vorbelan Roofing – Half Page Ad Concepts</title>
<link href="https://fonts.googleapis.com/css2?family=Anton&family=Open+Sans:ital,wght@0,400;0,600;0,700;0,800;1,400&display=swap" rel="stylesheet">
<style>
  :root{
    --ink:#111111;
    --band:#0c0c0c;
    --paper:#ffffff;
    --steel:#8c9096;
    --brand-blue:#3d6fb5;
    --link-blue:#2f5fb0;
    --label:#9a9a9a;
    --glove-1:#e8c25a;
    --glove-2:#c99a2e;
    --helmet:#f1f1f1;
  }
  *{box-sizing:border-box;margin:0;padding:0}
  html,body{width:1127px;height:1200px;overflow:hidden;background:var(--paper)}
  body{position:relative;font-family:"Open Sans",Arial,sans-serif;color:var(--ink)}

  .ad{position:absolute;width:518px;height:342px;overflow:hidden;background:var(--paper)}
  .ad--c1{left:33px}.ad--c2{left:581px}
  .ad--r1{top:41px}.ad--r2{top:425px}.ad--r3{top:811px}
  .ad__backdrop{position:absolute;inset:0;width:100%;height:100%}

  .concept-label{position:absolute;font-weight:700;font-size:18px;letter-spacing:.5px;color:var(--label)}

  .artwork{position:absolute;z-index:1;border-radius:50% 50% 18% 18%;
    background:linear-gradient(180deg,var(--glove-1) 0%,var(--glove-2) 42%,var(--helmet) 48%,#cfcfd2 100%)}

  .headline{position:absolute;z-index:2;font-family:"Anton",Impact,sans-serif;font-weight:400;color:var(--ink);line-height:1.1}
  .headline--lg{font-size:33px}
  .headline--md{font-size:27px}
  .kicker{position:absolute;z-index:2;font-size:11.5px;line-height:16px;color:var(--ink)}

  .copy{position:absolute;z-index:2;top:12px;width:234px}
  .copy__title{font-weight:700;font-size:11px;line-height:14px;margin-bottom:4px}
  .copy__body{font-size:8px;line-height:11px;color:#222}
  .copy__body p{text-indent:7px}
  .copy__body--plain p{text-indent:0}
  .copy__cta{font-weight:700;font-size:8.5px;line-height:12px;margin-top:4px}
  .copy__url{font-weight:700;font-size:11.5px;line-height:14px}

  .lead{position:absolute;z-index:2;left:222px;top:10px;width:288px}
  .lead__headline{font-family:"Anton",Impact,sans-serif;font-weight:400;font-size:33px;line-height:1.02;margin-bottom:6px}
  .lead__sub{font-weight:700;font-size:15.5px;line-height:19px}
  .lead__cta{font-size:11px;line-height:14px;margin-top:6px}
  .lead__url{font-weight:700;font-size:14px;line-height:17px;color:var(--link-blue)}

  .brand{position:absolute;left:22px;top:262px;display:flex;align-items:center;gap:8px}
  .brand__mark{width:18px;height:18px;background:var(--brand-blue)}
  .brand__name{font-weight:800;font-size:38px;line-height:1;color:var(--steel);letter-spacing:-1px}

  .contact{position:absolute;left:258px;top:258px;color:var(--paper)}
  .contact__intro{font-style:italic;font-size:10.5px;line-height:13px}
  .contact__line{display:flex;align-items:center;gap:4px;font-weight:700}
  .contact__line--phone{font-size:21px;line-height:24px}
  .contact__line--web{font-size:15px;line-height:19px}
  .contact__line svg{flex:none}

  .address{position:absolute;left:62px;top:322px;font-size:8.5px;line-height:11px;color:var(--paper);display:flex;gap:6px;align-items:center}

  .seal{position:absolute;left:434px;top:256px;width:66px;height:66px;border-radius:50%;
    background:radial-gradient(circle,#e6e6e6 0 55%,#8d8d8d 56% 100%)}
</style>
</head>
<body>

<svg width="0" height="0" style="position:absolute">
  <defs>
    <linearGradient id="skyGrad" x1="0" y1="0" x2="0" y2="1">
      <stop offset="0" stop-color="#ffffff"/><stop offset="0.5" stop-color="#ffffff"/><stop offset="1" stop-color="#c4c4c7"/>
    </linearGradient>
    <linearGradient id="ribbonGrad" x1="0" y1="0" x2="1" y2="0">
      <stop offset="0" stop-color="#c8c8cb"/><stop offset="1" stop-color="#f2f2f3"/>
    </linearGradient>
    <symbol id="backdrop" viewBox="0 0 518 342">
      <rect width="518" height="342" fill="url(#skyGrad)"/>
      <path d="M0 200 Q260 228 518 196 L518 222 Q260 248 0 240 Z" fill="url(#ribbonGrad)"/>
      <path d="M0 240 Q260 248 518 222 L518 342 L0 342 Z" fill="#0c0c0c"/>
    </symbol>
    <symbol id="iconPhone" viewBox="0 0 16 16"><circle cx="8" cy="8" r="8" fill="#fff"/><path d="M5 4l2 2-1 1.2c.6 1.2 1.6 2.2 2.8 2.8L10 9l2 2-1.2 1.2C7.5 11.8 4.2 8.5 3.8 5.2Z" fill="#0c0c0c"/></symbol>
    <symbol id="iconWeb" viewBox="0 0 16 16"><circle cx="8" cy="8" r="8" fill="#fff"/><circle cx="8" cy="8" r="5" fill="none" stroke="#0c0c0c" stroke-width="1.2"/><path d="M3 8h10M8 3v10" stroke="#0c0c0c" stroke-width="1.2"/></symbol>
    <symbol id="iconPin" viewBox="0 0 16 16"><circle cx="8" cy="8" r="8" fill="#3d6fb5"/><path d="M8 3.5a3 3 0 0 1 3 3c0 2.2-3 6-3 6s-3-3.8-3-6a3 3 0 0 1 3-3Z" fill="#fff"/></symbol>
    <symbol id="iconMail" viewBox="0 0 16 16"><circle cx="8" cy="8" r="8" fill="#3d6fb5"/><path d="M4 5.5h8v5H4Z M4 5.5l4 3 4-3" fill="none" stroke="#fff" stroke-width="1"/></symbol>
  </defs>
</svg>

<!-- DESIGN 1 -->
<section class="ad ad--c1 ad--r1">
  <svg class="ad__backdrop"><use href="#backdrop"/></svg>
  <div class="artwork" style="left:24px;top:12px;width:186px;height:200px" role="img" aria-label="Illustration of yellow work gloves resting on a white hard hat"></div>
  <div class="lead">
    <h2 class="lead__headline">Simply a harder<br>working roofing<br>company</h2>
    <p class="lead__sub">All types of large scale<br>apartment and condo, shingle<br>and flat roofing projects</p>
    <p class="lead__cta">Discover more online now at:</p>
    <p class="lead__url">www.vorbelan.com</p>
  </div>
  <div class="brand"><span class="brand__mark"></span><span class="brand__name">Vorbelan</span></div>
  <div class="contact">
    <p class="contact__intro">Call on our 30 years experience</p>
    <p class="contact__line contact__line--phone"><svg width="16" height="16"><use href="#iconPhone"/></svg>555.014.2290</p>
    <p class="contact__line contact__line--web"><svg width="15" height="15"><use href="#iconWeb"/></svg>www.vorbelan.com</p>
  </div>
  <div class="seal"></div>
  <p class="address"><svg width="11" height="11"><use href="#iconPin"/></svg>212 Harlow Avenue, Suite 40, Bramfield, TX 75010 <svg width="11" height="11"><use href="#iconMail"/></svg>info@vorbelan.com</p>
</section>
<p class="concept-label" style="left:33px;top:392px">DESIGN 1</p>

<!-- DESIGN 2 -->
<section class="ad ad--c2 ad--r1">
  <svg class="ad__backdrop"><use href="#backdrop"/></svg>
  <h2 class="headline headline--md" style="left:12px;top:10px;width:245px">It's the way we put<br>our roofing service<br>together that<br>sets us apart</h2>
  <div class="artwork" style="left:152px;top:116px;width:104px;height:92px" role="img" aria-label="Illustration of yellow work gloves resting on a white hard hat"></div>
  <div class="copy" style="left:268px">
    <p class="copy__title">All types of large scale apartment and condo, shingle and flat roofing projects</p>
    <div class="copy__body">
      <p>We're different. We have to be. We know that when it comes to roofing, there's tough competition for your business. That's why we pay the closest attention to every detail of our service from design to completion to ensure you are totally satisfied.</p>
      <p>This is a roofing service at a higher level. An affordable level that you'll only find at Vorbelan. And it doesn't take a lot to discover how affordable this quality is. Just a phone call. Our reputation is paramount. That's why we provide a service that is trusted to be on time and on budget, but above all reliable.</p>
    </div>
    <p class="copy__cta">Discover more online now at:</p>
    <p class="copy__url">www.vorbelan.com</p>
  </div>
  <div class="brand"><span class="brand__mark"></span><span class="brand__name">Vorbelan</span></div>
  <div class="contact">
    <p class="contact__intro">Call on our 30 years experience</p>
    <p class="contact__line contact__line--phone"><svg width="16" height="16"><use href="#iconPhone"/></svg>555.014.2290</p>
    <p class="contact__line contact__line--web"><svg width="15" height="15"><use href="#iconWeb"/></svg>www.vorbelan.com</p>
  </div>
  <div class="seal"></div>
  <p class="address"><svg width="11" height="11"><use href="#iconPin"/></svg>212 Harlow Avenue, Suite 40, Bramfield, TX 75010 <svg width="11" height="11"><use href="#iconMail"/></svg>info@vorbelan.com</p>
</section>
<p class="concept-label" style="left:581px;top:392px">DESIGN 2</p>

<!-- DESIGN 3 -->
<section class="ad ad--c1 ad--r2">
  <svg class="ad__backdrop"><use href="#backdrop"/></svg>
  <h2 class="headline headline--md" style="left:18px;top:10px;width:245px">The right choice of<br>roofing company is<br>not only important,<br>it's everything!</h2>
  <p class="kicker" style="left:18px;top:140px">Vorbelan makes the choice easy.</p>
  <div class="artwork" style="left:180px;top:160px;width:86px;height:62px" role="img" aria-label="Illustration of yellow work gloves resting on a white hard hat"></div>
  <div class="copy" style="left:274px">
    <p class="copy__title">All types of large scale apartment and condo, shingle and flat roofing projects</p>
    <div class="copy__body copy__body--plain">
      <p>Vorbelan Roofing Inc, more commonly known as Vorbelan, has been improving and adding value to multifamily apartment communities and student housing developments for over 30 years now. Although we have done work in many other states, most of our projects are in the great state of Texas. From the simple to the lavish, we've experienced it all and we can help you every step of the way. No job is too small or too big for our knowledgeable roofing crews.</p>
    </div>
    <p class="copy__cta">Discover more online now at:</p>
    <p class="copy__url">www.vorbelan.com</p>
  </div>
  <div class="brand"><span class="brand__mark"></span><span class="brand__name">Vorbelan</span></div>
  <div class="contact">
    <p class="contact__intro">Call on our 30 years experience</p>
    <p class="contact__line contact__line--phone"><svg width="16" height="16"><use href="#iconPhone"/></svg>555.014.2290</p>
    <p class="contact__line contact__line--web"><svg width="15" height="15"><use href="#iconWeb"/></svg>www.vorbelan.com</p>
  </div>
  <div class="seal"></div>
  <p class="address"><svg width="11" height="11"><use href="#iconPin"/></svg>212 Harlow Avenue, Suite 40, Bramfield, TX 75010 <svg width="11" height="11"><use href="#iconMail"/></svg>info@vorbelan.com</p>
</section>
<p class="concept-label" style="left:33px;top:775px">DESIGN 3</p>

<!-- DESIGN 4 -->
<section class="ad ad--c2 ad--r2">
  <svg class="ad__backdrop"><use href="#backdrop"/></svg>
  <h2 class="headline headline--md" style="left:22px;top:10px;width:215px">For the ultimate<br>roofing service<br>above call the<br>number<br>below</h2>
  <div class="artwork" style="left:150px;top:130px;width:110px;height:84px" role="img" aria-label="Illustration of yellow work gloves resting on a white hard hat"></div>
  <div class="copy" style="left:274px">
    <p class="copy__title">All types of large scale apartment and condo, shingle and flat roofing projects</p>
    <div class="copy__body copy__body--plain">
      <p>Vorbelan Roofing Inc, more commonly known as Vorbelan, has been improving and adding value to multifamily apartment communities and student housing developments for over 30 years now. Although we have done work in many other states, most of our projects are in the great state of Texas. From the simple to the lavish, we've experienced it all and we can help you every step of the way. No job is too small or too big for our knowledgeable roofing crews.</p>
    </div>
    <p class="copy__cta">Discover more online now at:</p>
    <p class="copy__url">www.vorbelan.com</p>
  </div>
  <div class="brand"><span class="brand__mark"></span><span class="brand__name">Vorbelan</span></div>
  <div class="contact">
    <p class="contact__intro">Call on our 30 years experience</p>
    <p class="contact__line contact__line--phone"><svg width="16" height="16"><use href="#iconPhone"/></svg>555.014.2290</p>
    <p class="contact__line contact__line--web"><svg width="15" height="15"><use href="#iconWeb"/></svg>www.vorbelan.com</p>
  </div>
  <div class="seal"></div>
  <p class="address"><svg width="11" height="11"><use href="#iconPin"/></svg>212 Harlow Avenue, Suite 40, Bramfield, TX 75010 <svg width="11" height="11"><use href="#iconMail"/></svg>info@vorbelan.com</p>
</section>
<p class="concept-label" style="left:581px;top:775px">DESIGN 4</p>

<!-- DESIGN 5 -->
<section class="ad ad--c1 ad--r3">
  <svg class="ad__backdrop"><use href="#backdrop"/></svg>
  <h2 class="headline headline--lg" style="left:18px;top:10px;width:245px">Simply a harder<br>working roofing<br>company</h2>
  <div class="artwork" style="left:160px;top:122px;width:104px;height:90px" role="img" aria-label="Illustration of yellow work gloves resting on a white hard hat"></div>
  <div class="copy" style="left:274px">
    <p class="copy__title">All types of large scale apartment and condo, shingle and flat roofing projects</p>
    <div class="copy__body">
      <p>We're different. We have to be. We know that when it comes to roofing, there's tough competition for your business. That's why we pay the closest attention to every detail of our service from design to completion to ensure you are totally satisfied.</p>
      <p>This is a roofing service at a higher level. An affordable level that you'll only find at Vorbelan. And it doesn't take a lot to discover how affordable this quality is. Just a phone call. Our reputation is paramount. That's why we provide a service that is trusted to be on time and on budget, but above all reliable.</p>
    </div>
    <p class="copy__cta">Discover more online now at:</p>
    <p class="copy__url">www.vorbelan.com</p>
  </div>
  <div class="brand"><span class="brand__mark"></span><span class="brand__name">Vorbelan</span></div>
  <div class="contact">
    <p class="contact__intro">Call on our 30 years experience</p>
    <p class="contact__line contact__line--phone"><svg width="16" height="16"><use href="#iconPhone"/></svg>555.014.2290</p>
    <p class="contact__line contact__line--web"><svg width="15" height="15"><use href="#iconWeb"/></svg>www.vorbelan.com</p>
  </div>
  <div class="seal"></div>
  <p class="address"><svg width="11" height="11"><use href="#iconPin"/></svg>212 Harlow Avenue, Suite 40, Bramfield, TX 75010 <svg width="11" height="11"><use href="#iconMail"/></svg>info@vorbelan.com</p>
</section>
<p class="concept-label" style="left:33px;top:1162px">DESIGN 5</p>

<!-- DESIGN 6 -->
<section class="ad ad--c2 ad--r3">
  <svg class="ad__backdrop"><use href="#backdrop"/></svg>
  <h2 class="headline headline--lg" style="left:18px;top:10px;width:245px">Simply a harder<br>working roofing<br>company</h2>
  <div class="artwork" style="left:160px;top:122px;width:104px;height:90px" role="img" aria-label="Illustration of yellow work gloves resting on a white hard hat"></div>
  <div class="copy" style="left:274px">
    <p class="copy__title">All types of large scale apartment and condo, shingle and flat roofing projects</p>
    <div class="copy__body copy__body--plain">
      <p>Vorbelan Roofing Inc, more commonly known as Vorbelan, has been improving and adding value to multifamily apartment communities and student housing developments for over 30 years now. Although we have done work in many other states, most of our projects are in the great state of Texas. From the simple to the lavish, we've experienced it all and we can help you every step of the way. No job is too small or too big for our knowledgeable roofing crews.</p>
    </div>
    <p class="copy__cta">Discover more online now at:</p>
    <p class="copy__url">www.vorbelan.com</p>
  </div>
  <div class="brand"><span class="brand__mark"></span><span class="brand__name">Vorbelan</span></div>
  <div class="contact">
    <p class="contact__intro">Call on our 30 years experience</p>
    <p class="contact__line contact__line--phone"><svg width="16" height="16"><use href="#iconPhone"/></svg>555.014.2290</p>
    <p class="contact__line contact__line--web"><svg width="15" height="15"><use href="#iconWeb"/></svg>www.vorbelan.com</p>
  </div>
  <div class="seal"></div>
  <p class="address"><svg width="11" height="11"><use href="#iconPin"/></svg>212 Harlow Avenue, Suite 40, Bramfield, TX 75010 <svg width="11" height="11"><use href="#iconMail"/></svg>info@vorbelan.com</p>
</section>
<p class="concept-label" style="left:581px;top:1162px">DESIGN 6</p>

</body>
</html>
```